Business Card

We are looking to re-create our business card. Attached is the company logo. we would like it to be back and front. for example one side with the persons information and the other side with the company logo. Be as creative as you would like but also keep in mind, we are a Health Insurance company and we need to look professional as well.
Industry/Entity Type
Business

```html
<!DOCTYPE html>
<html lang="en">
<head>
<meta charset="utf-8">
<title>Harbor Wellness Group – Business Card Designs</title>
<link rel="stylesheet" href="https://fonts.googleapis.com/css2?family=Cinzel:wght@600&family=Lato:wght@900&family=Open+Sans:wght@400;600;700&display=swap">
<style>
  :root {
    --backdrop: #3a2a22;
    --card: #ffffff;
    --brand-blue: #1b8fd2;
    --band-blue: #1f93d4;
    --soft-blue: #8fd0ef;
    --mark-grey: #8c8c8c;
    --icon-grey: #9a9a9a;
    --text-grey: #7d7d7d;
    --label: #ffffff;
  }
  * { box-sizing: border-box; margin: 0; padding: 0; }
  html, body { width: 1200px; height: 900px; overflow: hidden; }
  body {
    background: var(--backdrop);
    font-family: "Open Sans", Arial, sans-serif;
    position: relative;
  }
  .design-label {
    position: absolute;
    font-family: "Lato", Arial, sans-serif;
    font-weight: 900;
    font-size: 46px;
    color: var(--label);
    line-height: 1;
  }
  .design-label--one { left: 128px; top: 50px; }
  .design-label--two { left: 590px; top: 805px; }

  .card {
    position: absolute;
    width: 500px;
    height: 290px;
    background: var(--card);
    border-radius: 16px;
    overflow: hidden;
    box-shadow: 0 10px 24px rgba(0,0,0,.45);
  }
  .row-one .card { top: 115px; }
  .row-two .card { top: 480px; }
  .card--front { left: 60px; }
  .card--back  { left: 640px; }

  /* front side */
  .web-band {
    position: absolute; left: 0; top: 0; bottom: 0; width: 44px;
    background: var(--band-blue);
  }
  .web-band span {
    position: absolute; left: 50%; top: 50%;
    transform: translate(-50%, -50%) rotate(-90deg);
    white-space: nowrap;
    color: #fff; font-weight: 600; font-size: 13px;
  }
  .person {
    position: absolute; right: 24px; top: 20px; text-align: right;
    font-family: "Cinzel", Georgia, serif;
  }
  .person__name { color: var(--brand-blue); font-size: 17px; letter-spacing: .5px; }
  .person__role { color: var(--text-grey); font-size: 10px; letter-spacing: 1px; }
  .accent-square {
    position: absolute; width: 34px; height: 34px; border-radius: 4px;
    background: var(--soft-blue);
  }
  .company-name {
    position: absolute; color: var(--brand-blue); font-size: 26px; white-space: nowrap;
  }
  .wordmark {
    position: absolute; display: flex; align-items: center; gap: 6px;
    font-weight: 700; color: var(--mark-grey); letter-spacing: -1px;
  }
  .wordmark__dot { width: 12px; height: 12px; background: var(--brand-blue); border-radius: 2px; }
  .contact {
    position: absolute; left: 62px; bottom: 18px; list-style: none;
    font-size: 12px; font-weight: 600; color: var(--brand-blue);
  }
  .contact li { display: flex; align-items: center; gap: 8px; height: 22px; }
  .contact svg { width: 16px; height: 16px; flex: none; }
  .divider {
    position: absolute; width: 1px; height: 40px; background: #c6c6c6;
  }

  /* back side */
  .card--back .accent-square { width: 90px; height: 90px; border-radius: 8px; }
  .card--back .company-name { font-size: 36px; }
  .card--back .wordmark { font-size: 44px; }
  .card--back .wordmark__dot { width: 18px; height: 18px; }
</style>
</head>
<body>

<div class="design-label design-label--one">Design 1</div>

<section class="row-one">
  <article class="card card--front">
    <div class="web-band"><span>www.harborwellnessgroup.com</span></div>
    <div class="person">
      <div class="person__name">YOUR NAME</div>
      <div class="person__role">DESIGNATION</div>
    </div>
    <div class="accent-square" style="left:74px;top:58px;"></div>
    <div class="company-name" style="left:104px;top:104px;">Harbor Wellness Group</div>
    <div class="wordmark" style="right:24px;top:180px;font-size:32px;">HWG<span class="wordmark__dot"></span></div>
    <ul class="contact">
      <li><svg viewBox="0 0 16 16"><rect width="16" height="16" rx="2" fill="var(--icon-grey)"/><path d="M5 4h2l1 2.5-1.2.8a6 6 0 0 0 2 2l.8-1.2L12 9v2c0 .6-.4 1-1 1A7 7 0 0 1 4 5c0-.6.4-1 1-1z" fill="#fff"/></svg>+1 800-555-0142</li>
      <li><svg viewBox="0 0 16 16"><rect width="16" height="16" rx="2" fill="var(--icon-grey)"/><rect x="5" y="3" width="6" height="3" fill="#fff"/><rect x="3" y="6.5" width="10" height="4.5" rx="1" fill="#fff"/><rect x="5" y="10" width="6" height="3" fill="#fff" stroke="var(--icon-grey)" stroke-width=".8"/></svg>+33 (0)1 55 20 31 08</li>
      <li><svg viewBox="0 0 16 16"><rect width="16" height="16" rx="2" fill="var(--icon-grey)"/><rect x="3" y="4.5" width="10" height="7" fill="#fff"/><path d="M3 4.5l5 4 5-4" fill="none" stroke="var(--icon-grey)" stroke-width="1"/></svg>Info@northgateinvest.com</li>
    </ul>
  </article>

  <article class="card card--back">
    <div class="accent-square" style="left:110px;top:40px;"></div>
    <div class="wordmark" style="left:230px;top:80px;">HWG<span class="wordmark__dot"></span></div>
    <div class="company-name" style="left:50%;top:180px;transform:translateX(-50%);">Harbor Wellness Group</div>
  </article>
</section>

<section class="row-two">
  <article class="card card--front">
    <div class="web-band"><span>www.harborwellnessgroup.com</span></div>
    <div class="person">
      <div class="person__name">YOUR NAME</div>
      <div class="person__role">DESIGNATION</div>
    </div>
    <div class="wordmark" style="left:80px;top:98px;font-size:26px;">HWG<span class="wordmark__dot"></span></div>
    <div class="divider" style="left:172px;top:96px;"></div>
    <div class="company-name" style="left:186px;top:100px;font-size:21px;">Harbor Wellness Group</div>
    <div class="accent-square" style="right:30px;top:150px;width:44px;height:44px;"></div>
    <ul class="contact">
      <li><svg viewBox="0 0 16 16"><rect width="16" height="16" rx="2" fill="var(--icon-grey)"/><path d="M5 4h2l1 2.5-1.2.8a6 6 0 0 0 2 2l.8-1.2L12 9v2c0 .6-.4 1-1 1A7 7 0 0 1 4 5c0-.6.4-1 1-1z" fill="#fff"/></svg>+1 800-555-0142</li>
      <li><svg viewBox="0 0 16 16"><rect width="16" height="16" rx="2" fill="var(--icon-grey)"/><rect x="5" y="3" width="6" height="3" fill="#fff"/><rect x="3" y="6.5" width="10" height="4.5" rx="1" fill="#fff"/><rect x="5" y="10" width="6" height="3" fill="#fff" stroke="var(--icon-grey)" stroke-width=".8"/></svg>+33 (0)1 55 20 31 08</li>
      <li><svg viewBox="0 0 16 16"><rect width="16" height="16" rx="2" fill="var(--icon-grey)"/><rect x="3" y="4.5" width="10" height="7" fill="#fff"/><path d="M3 4.5l5 4 5-4" fill="none" stroke="var(--icon-grey)" stroke-width="1"/></svg>Info@northgateinvest.com</li>
    </ul>
  </article>

  <article class="card card--back">
    <div class="accent-square" style="left:110px;top:40px;"></div>
    <div class="wordmark" style="left:230px;top:80px;">HWG<span class="wordmark__dot"></span></div>
    <div class="company-name" style="left:50%;top:180px;transform:translateX(-50%);">Harbor Wellness Group</div>
  </article>
</section>

<div class="design-label design-label--two">Design 2</div>

</body>
</html>
```